Tending Our Garden eBook Cover Design

I want to deisgn a cover for my eBook (FRONT COVER) and the title is:

What I Grew From a Single Spark. And Why It Matters
By KT Dorran

TITLE CHANGED TO: UNDER THE WILLOW TREE; WHERE I FOUND MY QUIET STRENGTH AND WHERE YOU MIGHT TOO

The color palette is attached. Along with some photos options of me. Along with the ebook in WORD Document. My website is www.KTDorranLive.example. You can use a different color palette if you think it is best

Target Market(s)

women who look to build a personal brand

Industry/Entity Type

health and wellness

Requirements
Must have
• the title
Nice to have
• use my picture on the cover; but that is optional
Should not have
• any men

```html
<!DOCTYPE html>
<html lang="en">
<head>
<meta charset="utf-8">
<title>Tending Our Garden – eBook Cover</title>
<link href="https://fonts.googleapis.com/css2?family=Anton&family=Oswald:wght@500&family=Barlow+Semi+Condensed:wght@400&family=Allura&display=swap" rel="stylesheet">
<style>
  :root {
    --page: #ffffff;
    --cover-top: #8c5a52;
    --cover-mid: #74413b;
    --cover-bottom: #5c2b28;
    --sheen: rgba(255, 255, 255, 0.10);
    --blush: #f7cdd0;
    --white: #ffffff;
    --salmon: #ffb6a8;
    --tan: #dcc095;
    --rose: #eaa9a1;
    --photo-warm: #e8321f;
    --photo-dark: #2a1a18;
  }
  * { margin: 0; padding: 0; box-sizing: border-box; }
  html, body {
    width: 1200px;
    height: 815px;
    overflow: hidden;
    background: var(--page);
  }
  .canvas {
    position: relative;
    width: 1200px;
    height: 815px;
  }
  .cover {
    position: absolute;
    left: 348px;
    top: 28px;
    width: 504px;
    height: 760px;
    overflow: hidden;
    background:
      linear-gradient(125deg, var(--sheen) 0%, rgba(255,255,255,0.04) 38%, transparent 38.2%),
      linear-gradient(180deg, var(--cover-top) 0%, var(--cover-mid) 50%, var(--cover-bottom) 100%);
  }
  .author-photo {
    position: absolute;
    left: 0;
    top: 250px;
    width: 360px;
    height: 510px;
    border-radius: 160px 160px 0 0;
    background: linear-gradient(180deg, var(--photo-dark) 0%, var(--photo-dark) 32%, var(--photo-warm) 62%, var(--photo-warm) 100%);
  }
  .title {
    position: absolute;
    left: 20px;
    right: 20px;
    top: 26px;
    display: flex;
    flex-direction: column;
    align-items: center;
    font-weight: 400;
  }
  .title-kicker {
    font-family: "Barlow Semi Condensed", sans-serif;
    font-size: 16px;
    letter-spacing: 2.5px;
    line-height: 1;
    color: var(--blush);
    white-space: nowrap;
  }
  .title-lead {
    margin-top: 6px;
    font-family: "Anton", sans-serif;
    font-size: 82px;
    line-height: 0.95;
    letter-spacing: 1px;
    color: var(--white);
  }
  .title-row {
    display: flex;
    align-items: center;
    gap: 12px;
    margin-top: 2px;
  }
  .title-focus {
    font-family: "Anton", sans-serif;
    font-size: 86px;
    line-height: 0.95;
    color: var(--salmon);
    white-space: nowrap;
  }
  .title-tail {
    font-family: "Anton", sans-serif;
    font-size: 28px;
    line-height: 1.02;
    color: var(--tan);
    white-space: nowrap;
  }
  .byline {
    position: absolute;
    left: 372px;
    top: 232px;
    font-family: "Allura", cursive;
    font-size: 72px;
    line-height: 1;
    color: var(--white);
  }
  .author {
    position: absolute;
    right: 32px;
    top: 318px;
    font-family: "Oswald", sans-serif;
    font-weight: 500;
    font-size: 52px;
    line-height: 1;
    color: var(--rose);
  }
</style>
</head>
<body>
  <main class="canvas">
    <section class="cover" aria-label="eBook front cover">
      <div class="author-photo" role="img" aria-label="Portrait photo of the author, seated in a red dress and smiling"></div>
      <h1 class="title">
        <span class="title-kicker">UNDER THE WILLOW TREE; WHERE I FOUND MY</span>
        <span class="title-lead">QUIET</span>
        <span class="title-row">
          <span class="title-focus">STRENGTH</span>
          <span class="title-tail">AND WHERE<br>YOU MIGHT<br>TOO</span>
        </span>
      </h1>
      <p class="byline">by</p>
      <p class="author">KT DORRAN</p>
    </section>
  </main>
</body>
</html>
```